Web Design Job: Facial Surgery Center (Valorin)--Web Design Needed

We need a web design for Valorin Facial Surgery. Valorin is in Chesterfield, MO (suburb of St. Louis), and is owned by a double board certified facial plastic surgeon and ENT. The website must feature a before and after photo book, a section for patient reviews, drop down menus that outline services offered (one for surgical procedures and one for office/nonsurgical procedures), and "About the Practice" section, a section to talk about the doctor and his staff, a "What's New" section, a section for information for out of town patients, as well as a link to the Medical Spa also owned by the doctor, as well as Facebook and Twitter. We are open to ideas regarding adding a "tour of the surgery center", featuring video footage of the state of the art facility, as well as other video options. We prefer soothing colors such as aquas and blues, light greys, chocolate browns, etc (does not have to follow the color scheme in the attached logo). We would like the design to be easy to digest and informative, but not "thick". It should be an upscale, classy design that will appeal to all age brackets, but especially middle-aged women, as that is the primary clientele.

Target Market(s)

Middle aged women are our most common client, however, younger patients, both male and female, will often visit the site for select procedures.

Industry/Entity Type

Medical

Number of Pages Required

5+ page

Font styles to use
Sans Serif

Colors
86cfc6
85cae6
cee9f5
cfeae6
edf8f6
85acd3
cfdfed

Requirements
Must have
• Before and after picture book, links to Facebook, Twitter and Instagram, a soothing, peaceful aesthetic, a page for reviews, as well as a link to reviews on Yelp or similar page.
Nice to have
• Drop down menus that include the surgical and nonsurgical procedures. Each surgical procedure could have it's own section that includes a before and after picture book.
Should not have
• Too many words!

```html
<!DOCTYPE html>
<html lang="en">
<head>
<meta charset="utf-8">
<title>Valorin Facial Surgery</title>
<link href="https://fonts.googleapis.com/css2?family=Lato:wght@300;400;700;900&display=swap" rel="stylesheet">
<style>
:root{
  --teal:#3fb6c4;
  --teal-deep:#2a9fb0;
  --aqua:#86cfc6;
  --sky:#85cae6;
  --mist:#edf8f6;
  --ink:#333a40;
  --muted:#7a8288;
  --line:#d9dde0;
  --footer:#2b2d2f;
  --footer-deep:#1f2022;
  --white:#ffffff;
}
*{box-sizing:border-box;margin:0;padding:0}
html,body{width:1200px;height:2456px;overflow:hidden}
body{font-family:'Lato',sans-serif;color:var(--ink);background:var(--white)}
.page{width:1200px;height:2456px;position:relative}

/* hero */
.hero{position:relative;height:560px;overflow:hidden}
.hero-photo{position:absolute;inset:0;background:linear-gradient(100deg,#9fb59a 0%,#c6cfb2 35%,#e8d8c8 55%,#c99a7e 75%,#8e7463 100%)}
.site-header{position:absolute;top:0;left:0;right:0;height:70px;display:flex;align-items:center;justify-content:space-between;padding:0 40px;background:rgba(255,255,255,.12)}
.brand{display:flex;align-items:center;gap:10px;color:var(--white)}
.brand-dot{width:12px;height:12px;border-radius:50%;background:var(--white)}
.brand-name{font-size:30px;font-weight:700;letter-spacing:1px;line-height:1}
.brand-sub{font-size:10px;letter-spacing:4px;font-weight:400;margin-top:2px}
.header-tools{display:flex;align-items:center;gap:22px;color:var(--white);font-size:15px}
.header-tools span{display:flex;align-items:center;gap:8px}
.hero-circle{position:absolute;left:70px;top:120px;width:330px;height:330px;border-radius:50%;background:rgba(255,255,255,.82);box-shadow:0 0 0 14px rgba(255,255,255,.35);display:flex;flex-direction:column;justify-content:center;padding-left:52px}
.hero-kicker{font-size:30px;font-weight:900;color:var(--teal);line-height:1.15}
.hero-rule{width:200px;height:2px;background:var(--teal);margin:18px 0}
.hero-title{font-size:24px;font-weight:700;color:var(--teal-deep);line-height:1.3}
.hero-dots{position:absolute;right:70px;bottom:34px;display:flex;gap:8px}
.hero-dots i{width:10px;height:10px;border-radius:50%;background:rgba(255,255,255,.6)}
.hero-dots i:first-child{background:var(--white)}

/* welcome */
.welcome{height:440px;display:flex;gap:60px;padding:64px 80px 0;background:var(--white)}
.welcome-text{flex:1}
.welcome-title{font-size:30px;font-weight:700;color:var(--ink);display:flex;align-items:baseline;gap:10px}
.welcome-title b{color:var(--teal);font-size:36px}
.welcome-rule{width:340px;height:2px;background:var(--line);margin:12px 0 20px}
.welcome-text p{font-size:13px;line-height:1.75;color:var(--muted);margin-bottom:16px}
.btn{display:inline-block;padding:9px 20px;font-size:12px;border:1px solid #9aa0a5;color:var(--ink);background:var(--white)}
.welcome-media{width:400px;height:320px;position:relative;padding:10px;background:linear-gradient(135deg,#6c5a8e,#a39cc4)}
.welcome-photo{width:100%;height:100%;background:linear-gradient(120deg,#e9e3ee,#d6c1b4 60%,#b89a8a)}
.media-arrows{position:absolute;right:18px;bottom:18px;display:flex;gap:4px}
.media-arrows span{width:26px;height:26px;background:rgba(40,40,60,.75);display:flex;align-items:center;justify-content:center}

/* procedures */
.procedures{height:460px;display:flex}
.procedure{flex:1;padding:38px 60px;color:var(--white);position:relative}
.procedure.surgical{background:linear-gradient(135deg,#2e3f52,#4a6a86)}
.procedure.non-surgical{background:linear-gradient(135deg,#2f7fbd,#5fb4e0 60%,#9ad6ec)}
.procedure h2{font-size:28px;font-weight:400;letter-spacing:.5px}
.procedure-rule{width:100%;height:1px;background:rgba(255,255,255,.5);margin:10px 0 22px}
.procedure-photo{width:100%;height:200px}
.surgical .procedure-photo{background:linear-gradient(120deg,#8fa7bd,#d9c2b4 55%,#b7a59a)}
.non-surgical .procedure-photo{background:linear-gradient(120deg,#f1ede6,#e7c7b4 50%,#a6c7d8)}
.procedure p{font-size:12.5px;line-height:1.7;margin:18px 0;color:rgba(255,255,255,.9)}
.procedure .btn{background:transparent;color:var(--white);border-color:rgba(255,255,255,.8)}

/* team */
.team{height:400px;background:linear-gradient(180deg,#f7f7f7,#eceeef);text-align:center;padding-top:36px}
.section-title{display:flex;align-items:center;justify-content:center;gap:18px;font-size:28px;font-weight:700;color:var(--ink)}
.section-title::before,.section-title::after{content:"";width:120px;height:1px;background:#9aa0a5}
.team-row{display:flex;justify-content:center;align-items:flex-start;gap:46px;margin-top:40px}
.member{width:160px}
.avatar{width:150px;height:150px;border-radius:50%;margin:0 auto;border:5px solid var(--white);box-shadow:0 2px 8px rgba(0,0,0,.15);background:linear-gradient(150deg,#d9c1ae,#a07a64)}
.member.featured .avatar{width:170px;height:170px;margin-top:-10px;background:linear-gradient(150deg,#3b3b3b,#151515);display:flex;align-items:center;justify-content:center;gap:8px}
.member.featured .avatar i{width:26px;height:26px;border-radius:50%;background:rgba(255,255,255,.9)}
.member.featured h3{margin-top:8px}
.member h3{font-size:17px;font-weight:700;margin-top:18px}
.member p{font-size:12px;color:var(--muted);margin-top:4px}

/* testimonials */
.testimonials{height:280px;text-align:center;padding-top:36px;background:var(--white)}
.testimonials h2{font-size:30px;font-weight:700}
.testimonials .sub{font-size:13px;color:var(--muted);letter-spacing:1px;margin-top:4px}
.divider{width:240px;height:12px;margin:10px auto 0;display:block}
.quote{display:flex;align-items:center;gap:30px;width:1000px;margin:28px auto 0;text-align:left}
.quote-avatar{width:100px;height:100px;border-radius:50%;flex:none;background:linear-gradient(150deg,#8a5a48,#3a2a24)}
.quote p{font-size:13px;line-height:1.75;color:var(--muted);font-style:italic}
.quote cite{display:block;margin-top:8px;font-style:normal;font-size:13px;color:var(--ink)}
.quote cite b{margin-right:10px}

/* footer */
.site-footer{height:316px;background:var(--footer);color:#cfd3d6;padding:40px 60px 0;display:flex;gap:60px;position:relative}
.footer-col h4{font-size:16px;font-weight:700;color:var(--white);margin-bottom:14px}
.footer-col ul{list-style:none;font-size:13px;line-height:1.9}
.footer-col ul li::before{content:"› ";color:var(--aqua)}
.hours-row{display:flex;align-items:center;gap:12px;margin-bottom:18px}
.hours-row strong{font-size:30px;font-weight:400;color:var(--white)}
.hours-row small{font-size:17px;color:var(--white)}
.hours-row em{display:block;font-style:normal;font-size:11px;color:#9aa0a5}
.contact-row{display:flex;gap:12px;font-size:12.5px;line-height:1.55;margin-bottom:10px;align-items:flex-start}
.footer-brand{margin-left:auto;text-align:right;padding-top:10px}
.footer-brand .brand{justify-content:flex-end}
.socials{display:flex;gap:10px;justify-content:flex-end;margin-top:22px}
.socials i{width:28px;height:28px;background:var(--white);border-radius:3px}
.copyright{position:absolute;left:0;right:0;bottom:0;height:40px;background:var(--footer-deep);color:#8e9498;font-size:12px;display:flex;align-items:center;justify-content:center}
</style>
</head>
<body>
<div class="page">

  <section class="hero">
    <div class="hero-photo" role="img" aria-label="Smiling woman with a white towel wrapped on her hair, soft green garden background"></div>
    <header class="site-header">
      <div class="brand">
        <span class="brand-dot"></span>
        <div><div class="brand-name">Valorin</div><div class="brand-sub">FACIAL SURGERY</div></div>
      </div>
      <div class="header-tools">
        <span>
          <svg width="16" height="16" viewBox="0 0 24 24" fill="#fff"><path d="M6.6 10.8a15 15 0 0 0 6.6 6.6l2.2-2.2a1 1 0 0 1 1-.25 11.4 11.4 0 0 0 3.6.57 1 1 0 0 1 1 1V20a1 1 0 0 1-1 1A17 17 0 0 1 3 4a1 1 0 0 1 1-1h3.5a1 1 0 0 1 1 1c0 1.25.2 2.45.57 3.57a1 1 0 0 1-.25 1z"/></svg>
          123-456-7890
        </span>
        <svg width="22" height="16" viewBox="0 0 22 16" fill="#fff"><rect width="22" height="2.5"/><rect y="6.7" width="22" height="2.5"/><rect y="13.5" width="22" height="2.5"/></svg>
        <svg width="18" height="18" viewBox="0 0 24 24" fill="none" stroke="#fff" stroke-width="2.5"><circle cx="10" cy="10" r="7"/><path d="M15 15l7 7"/></svg>
      </div>
    </header>
    <div class="hero-circle">
      <div class="hero-kicker">WE CREATE<br>PERFECTION</div>
      <div class="hero-rule"></div>
      <div class="hero-title">FACIAL SURGERY<br>PROCEDURES</div>
    </div>
    <div class="hero-dots"><i></i><i></i><i></i></div>
  </section>

  <section class="welcome">
    <div class="welcome-text">
      <h1 class="welcome-title">WELCOME TO <b>Valorin</b></h1>
      <div class="welcome-rule"></div>
      <p>Our practice offers gentle, natural facial care in a calm and private setting. Every plan is shaped around your goals, your comfort and your schedule, so results feel like you at your very best.</p>
      <p>From first consultation to final follow-up, our board certified surgeon and caring team guide you through each step with clear answers and honest advice.</p>
      <p>Visit our center to meet the team, tour the suite and learn which treatments suit you best.</p>
      <span class="btn">Read More</span>
    </div>
    <div class="welcome-media">
      <div class="welcome-photo" role="img" aria-label="Woman with bare shoulders touching her face, soft pastel backdrop"></div>
      <div class="media-arrows">
        <span><svg width="10" height="12" viewBox="0 0 10 12"><path d="M8 1L2 6l6 5" stroke="#fff" stroke-width="2" fill="none"/></svg></span>
        <span><svg width="10" height="12" viewBox="0 0 10 12"><path d="M2 1l6 5-6 5" stroke="#fff" stroke-width="2" fill="none"/></svg></span>
      </div>
    </div>
  </section>

  <section class="procedures">
    <article class="procedure surgical">
      <h2>SURGICAL PROCEDURES</h2>
      <div class="procedure-rule"></div>
      <div class="procedure-photo" role="img" aria-label="Close view of a woman's face being marked before surgery"></div>
      <p>Facelift, brow lift, eyelid and nose surgery performed with care and precision. Each plan aims for refreshed, balanced and natural looking results.</p>
      <span class="btn">Read more</span>
    </article>
    <article class="procedure non-surgical">
      <h2>NON SURGICAL PROCEDURES</h2>
      <div class="procedure-rule"></div>
      <div class="procedure-photo" role="img" aria-label="Woman relaxing during a facial mask treatment at a spa"></div>
      <p>Injectables, peels, laser and skin care treatments with little downtime. Gentle options that renew your skin and keep you looking rested.</p>
      <span class="btn">Read more</span>
    </article>
  </section>

  <section class="team">
    <h2 class="section-title">OUR TEAM</h2>
    <div class="team-row">
      <div class="member"><div class="avatar" role="img" aria-label="Portrait of team member Nora"></div><h3>Nora</h3><p>Patient care lead</p></div>
      <div class="member"><div class="avatar" role="img" aria-label="Portrait of team member Jade"></div><h3>Jade</h3><p>Nurse specialist</p></div>
      <div class="member featured"><div class="avatar" role="img" aria-label="Portrait of team member Maren with social links"><i></i><i></i><i></i></div><h3>Maren</h3><p>Lead surgeon</p></div>
      <div class="member"><div class="avatar" role="img" aria-label="Portrait of team member Alba"></div><h3>Alba</h3><p>Skin therapist</p></div>
      <div class="member"><div class="avatar" role="img" aria-label="Portrait of team member Esme"></div><h3>Esme</h3><p>Office manager</p></div>
    </div>
  </section>

  <section class="testimonials">
    <h2>TESTIMONIALS</h2>
    <div class="sub">WHAT OUR PEOPLE SAY</div>
    <svg class="divider" viewBox="0 0 240 12"><line x1="0" y1="6" x2="105" y2="6" stroke="#9aa0a5"/><circle cx="120" cy="6" r="4" fill="none" stroke="#9aa0a5"/><line x1="135" y1="6" x2="240" y2="6" stroke="#9aa0a5"/></svg>
    <div class="quote">
      <div class="quote-avatar" role="img" aria-label="Portrait of patient Lena Morrow"></div>
      <div>
        <p>“From my first visit I felt heard and at ease. The team explained every step, the recovery was easier than I expected, and the result looks so natural that friends only say I look rested. I could not be happier with my choice and the warm care I received.”</p>
        <cite><b>Lena Morrow</b>Designer, St. Louis</cite>
      </div>
    </div>
  </section>

  <footer class="site-footer">
    <div class="footer-col">
      <h4>Quick Link</h4>
      <ul><li>Home</li><li>About Us</li><li>Services</li><li>Reviews</li><li>Team</li><li>Contact Us</li></ul>
    </div>
    <div class="footer-col">
      <h4>Opening Hours</h4>
      <div class="hours-row">
        <svg width="30" height="30" viewBox="0 0 24 24" fill="none" stroke="#fff" stroke-width="1.6"><circle cx="12" cy="12" r="10"/><path d="M12 6v6l4 2"/></svg>
        <div><strong>9:00am</strong> <small>To 7:00pm</small><em>Monday to Saturday</em></div>
      </div>
      <div class="hours-row">
        <svg width="30" height="30" viewBox="0 0 24 24" fill="none" stroke="#fff" stroke-width="1.6"><circle cx="12" cy="12" r="10"/><path d="M12 6v6l4 2"/></svg>
        <div><strong>8:00am</strong> <small>To 4:00pm</small><em>Sunday &amp; Public holiday</em></div>
      </div>
    </div>
    <div class="footer-col">
      <h4>Contact Address</h4>
      <div class="contact-row">
        <svg width="14" height="18" viewBox="0 0 14 18" fill="#fff"><path d="M7 0a7 7 0 0 0-7 7c0 5 7 11 7 11s7-6 7-11a7 7 0 0 0-7-7zm0 10a3 3 0 1 1 0-6 3 3 0 0 1 0 6z"/></svg>
        <div>VALORIN FACIAL SURGERY<br>210 Clarkson Lane, Suite 4<br>Chesterfield, MO</div>
      </div>
      <div class="contact-row">
        <svg width="14" height="14" viewBox="0 0 24 24" fill="#fff"><path d="M6.6 10.8a15 15 0 0 0 6.6 6.6l2.2-2.2a1 1 0 0 1 1-.25 11.4 11.4 0 0 0 3.6.57 1 1 0 0 1 1 1V20a1 1 0 0 1-1 1A17 17 0 0 1 3 4a1 1 0 0 1 1-1h3.5a1 1 0 0 1 1 1c0 1.25.2 2.45.57 3.57a1 1 0 0 1-.25 1z"/></svg>
        <div>123-456-7890<br>123-456-7890</div>
      </div>
      <div class="contact-row">
        <svg width="16" height="12" viewBox="0 0 16 12" fill="none" stroke="#fff" stroke-width="1.4"><rect x=".7" y=".7" width="14.6" height="10.6"/><path d="M1 1l7 6 7-6"/></svg>
        <div>hello@valorinsurgery.com</div>
      </div>
    </div>
    <div class="footer-brand">
      <div class="brand">
        <span class="brand-dot"></span>
        <div><div class="brand-name">Valorin</div><div class="brand-sub">FACIAL SURGERY</div></div>
      </div>
      <div class="socials"><i></i><i></i><i></i><i></i></div>
    </div>
    <div class="copyright">© 2015 Valorin Facial Surgery . All Rights Reserved</div>
  </footer>
</div>
</body>
</html>
```